Cedar Ridge Paving. Chip Seal Done Right

I need my card to have all my basic information on it. Keep it simple. Include web site, phone number and email address. Include phrase Chip Seal Done Right or Cedar Ridge’s Top Paving Company. Keep card simple. Include color and logo. Put all contact info on card. Make card simple and not complicated.
Updates

Here is infuriation yo out in business card

Mark T. Delgado
512.408.7316 cell phone
Markdelgado7@mailbrook.net
www.cedarridgepaving.net

Target Market(s)

Hill Country Texas USA

Industry/Entity Type

Road chip seal

Contact Information for Business Card

We chip seal roads for ranches and property owners

Font styles to use
Serif
Sans Serif
Decorative
Script

Colors
0054AA
0677BA
7BADD7
CADEEF
E8F1F8
EB3D1F
EC4F4E
F09395
F8D3D4
FCEDEE

Requirements
Must have
• Keep it simply
Nice to have
• Logo and all basic info

```html
<!DOCTYPE html>
<html lang="en">
<head>
<meta charset="utf-8">
<title>Cedar Ridge Paving — Business Card</title>
<link href="https://fonts.googleapis.com/css2?family=Montserrat:wght@400;500;600;800&display=swap" rel="stylesheet">
<style>
  :root {
    --navy: #1b2258;
    --red: #c2202f;
    --paper: #f4f4f3;
    --backdrop: #202020;
    --rule: #b9b9b9;
  }
  * { box-sizing: border-box; margin: 0; padding: 0; }
  html, body { width: 1200px; height: 900px; overflow: hidden; }
  body {
    background: var(--backdrop);
    font-family: "Montserrat", Arial, sans-serif;
    position: relative;
  }
  .card {
    position: absolute;
    width: 560px;
    height: 320px;
    border-radius: 4px;
    box-shadow: 0 12px 30px rgba(0,0,0,.55);
  }
  .card--back {
    left: 590px; top: 100px;
    background: var(--navy);
    display: flex; align-items: center; justify-content: center;
  }
  .card--front {
    left: 50px; top: 480px;
    background: var(--paper);
    display: flex; align-items: center;
  }
  .brand { display: flex; flex-direction: column; align-items: flex-start; }
  .brand__row { display: flex; align-items: center; gap: 10px; }
  .brand__mark { width: 26px; height: 26px; background: var(--red); }
  .brand__name {
    font-weight: 800; text-transform: uppercase;
    line-height: 1.05; letter-spacing: .5px;
  }
  .brand__rule { height: 1px; background: var(--red); margin-top: 8px; }
  .brand__tagline {
    font-size: 8px; color: var(--red); letter-spacing: 1px;
    text-transform: uppercase; margin-top: 4px; font-weight: 500;
  }
  .card--back .brand__name { color: #fff; font-size: 28px; }
  .card--back .brand__rule { width: 230px; }
  .card--front .brand__name { color: var(--navy); font-size: 20px; }
  .card--front .brand__rule { width: 170px; }

  .front__brand { width: 250px; padding-left: 34px; }
  .front__divider { width: 1px; height: 170px; background: var(--rule); }
  .contact { padding-left: 26px; color: var(--navy); }
  .contact__name {
    color: var(--red); font-weight: 600; font-size: 17px;
    text-transform: uppercase; letter-spacing: .4px;
  }
  .contact__title { font-size: 12px; margin-bottom: 14px; }
  .contact__list { list-style: none; font-size: 11.5px; }
  .contact__item { display: flex; align-items: center; gap: 8px; margin-bottom: 5px; }
  .contact__item svg { width: 12px; height: 12px; fill: none; stroke: var(--red); stroke-width: 2; }
  .contact__address { font-size: 11.5px; margin-top: 12px; line-height: 1.4; padding-left: 20px; }
</style>
</head>
<body>

  <section class="card card--back" aria-label="Card back">
    <div class="brand">
      <div class="brand__row">
        <span class="brand__mark"></span>
        <span class="brand__name">Cedar Ridge Paving</span>
      </div>
      <div class="brand__rule"></div>
      <span class="brand__tagline">Over 40 years</span>
    </div>
  </section>

  <section class="card card--front" aria-label="Card front">
    <div class="front__brand">
      <div class="brand">
        <div class="brand__row">
          <span class="brand__mark"></span>
          <span class="brand__name">Cedar Ridge<br>Paving</span>
        </div>
        <div class="brand__rule"></div>
        <span class="brand__tagline">Over 40 years</span>
      </div>
    </div>
    <div class="front__divider"></div>
    <div class="contact">
      <p class="contact__name">Mark T. Delgado</p>
      <p class="contact__title">Managing Director</p>
      <ul class="contact__list">
        <li class="contact__item">
          <svg viewBox="0 0 24 24"><path d="M5 3h4l2 5-3 2a12 12 0 0 0 6 6l2-3 5 2v4a2 2 0 0 1-2 2A18 18 0 0 1 3 5a2 2 0 0 1 2-2z"/></svg>
          512.408.7316
        </li>
        <li class="contact__item">
          <svg viewBox="0 0 24 24"><rect x="2" y="5" width="20" height="14"/><path d="M2 5l10 8 10-8"/></svg>
          Markdelgado7@mailbrook.net
        </li>
        <li class="contact__item">
          <svg viewBox="0 0 24 24"><circle cx="12" cy="12" r="10"/><path d="M2 12h20M12 2c3 3 3 17 0 20M12 2c-3 3-3 17 0 20"/></svg>
          www.cedarridgepaving.net
        </li>
      </ul>
      <p class="contact__address">218 Ranch Road 12,<br>Wimberley TX 78676</p>
    </div>
  </section>

</body>
</html>
```